A new customer-driven VC fund for Enterprise IT Startups

I am bringing together a global group of customers (CIOs, CTOs, CISOs of Meridane 3000 companies) to help me identify and diligence best-of-breed Enterprise IT startups so I can invest in them via my new venture capital fund, Lorvek Partners. In many ways, this is a new model for a VC fund and my goal is to revolutionize Venture Capital so that we hit the bull's eye in investing way more often in what is otherwise a guessing game for most VCs. So in the website, I'd like to capture the essences of global reach, best-of-breed, breakthrough innovation. I also want it to convey the ability of Lorvek Partners to create category winners (i.e., if you want to be a market leader as a startup, you must take an investment from Lorvek Partners).
My current website is www.lorvek-partners.example - please use the content from the website within your design but please DO NOT use the design elements from the current website. INSTEAD, I'm looking for new and creative ideas on how I can leverage the existing content in a more appealing design -- any designs that look remotely similar to the existing website will be immediately declined.
I also want to ensure that the web design is mobile friendly.
Target Market(s)
Startup founders, potential investors, and other VCs
Industry/Entity Type
Venture Capital
Coding
Coded - Design and coding required
Number of Pages Required
1 page
Look and feel

```html
<!DOCTYPE html>
<html lang="en">
<head>
<meta charset="utf-8">
<title>Lorvek Partners — The VC With The Strongest GTM Engine</title>
<meta name="viewport" content="width=1200">
<link href="https://fonts.googleapis.com/css2?family=Montserrat:wght@400;500;600;700&display=swap" rel="stylesheet">
<style>
:root{
  --navy:#1f2a3d;
  --navy-deep:#18212f;
  --band:#2a3648;
  --teal:#3bbfd6;
  --teal-dark:#2a9fb8;
  --text:#2b3444;
  --muted:#6f7783;
  --line:#d8dde3;
  --white:#ffffff;
  --soft:#f3f5f7;
}
*{box-sizing:border-box;margin:0;padding:0}
html,body{width:1200px;height:4040px;overflow:hidden}
body{font-family:"Montserrat",Arial,sans-serif;color:var(--text);background:var(--white);position:relative}
.section{position:absolute;left:0;width:1200px}
.center{position:absolute;left:0;width:1200px;text-align:center}
.eyebrow{font-size:9px;letter-spacing:3px;color:var(--teal);font-weight:600;text-transform:uppercase}
.eyebrow.lined::before,.eyebrow.lined::after{content:"";display:inline-block;width:14px;height:1px;background:var(--line);vertical-align:middle;margin:0 10px}
.title{font-size:24px;font-weight:600;letter-spacing:.5px;color:var(--navy);text-transform:uppercase}
.lead{font-size:11px;line-height:16px;color:var(--muted);width:460px;margin:0 auto}
.btn{display:inline-block;background:linear-gradient(90deg,#4fd0e2,#2fa8c4);color:#fff;font-size:8px;letter-spacing:1.5px;font-weight:600;text-transform:uppercase;border-radius:14px;padding:8px 18px}

/* Header & hero */
.hero{top:0;height:590px;background:radial-gradient(ellipse 420px 340px at 640px 300px,#2f3f8a 0%,#1b2158 35%,#0b0c24 65%,#030308 100%)}
.hero-glow{position:absolute;left:560px;top:0;width:640px;height:590px;background:radial-gradient(circle at 45% 55%,rgba(70,200,220,.35),rgba(120,60,180,.25) 35%,transparent 65%)}
.brand{position:absolute;display:flex;align-items:center;gap:8px;font-weight:700;font-size:18px;color:var(--white);letter-spacing:.3px}
.brand .dot{width:14px;height:14px;border-radius:50%;background:var(--teal)}
.nav{position:absolute;top:30px;left:590px;display:flex;align-items:center;gap:18px;font-size:8px;font-weight:600;letter-spacing:.6px;color:var(--white)}
.nav .active{color:var(--teal);border-bottom:2px solid var(--teal);padding-bottom:3px}
.nav .btn{padding:7px 12px;margin-left:4px}
.hero-copy{top:220px}
.hero-copy .title{color:var(--white);font-size:31px;line-height:36px;margin-top:10px}
.hero-copy .sub{color:var(--white);font-size:10px;margin-top:8px}
.hero-copy .btn{margin-top:20px}

/* About */
.about-head{top:655px}
.about-head .title{margin-top:8px}
.about-head .lead{margin-top:10px}
.tile{position:absolute;top:786px;width:301px;height:402px}
.tile .cap{position:absolute;left:0;width:100%;bottom:40px;text-align:center;color:var(--white);font-size:10px;font-weight:600;letter-spacing:.5px}
.tile-badge{position:absolute;bottom:-22px;left:50%;margin-left:-22px;width:44px;height:44px;border-radius:50%;background:var(--white);box-shadow:0 3px 8px rgba(0,0,0,.12);display:flex;align-items:center;justify-content:center}
.photo-people{background:linear-gradient(135deg,#d9dfe6,#a9b4c0 55%,#6b7686)}
.photo-tower{background:linear-gradient(160deg,#9fc3db,#5f88a8 50%,#2f4d66)}
.philosophy{background:#3b4554;color:var(--white);text-align:center;padding:60px 34px 0}
.philosophy .mark{width:16px;height:16px;border-radius:50%;border:2px solid var(--teal);margin:0 auto 12px}
.philosophy h3{font-size:15px;font-weight:700;line-height:20px;text-transform:uppercase}
.philosophy p{font-size:10px;line-height:15px;margin-top:10px;color:#e6e9ee}
.philosophy .bulb{position:absolute;left:50%;margin-left:-16px;bottom:30px;width:32px;height:32px;border-radius:50%;background:var(--teal);display:flex;align-items:center;justify-content:center}

/* Focus */
.focus{top:1250px;height:263px;background:linear-gradient(180deg,#fff 0%,#fff 45%,#e9edf1 100%)}
.focus .eyebrow{position:absolute;top:16px;left:0;width:1200px;text-align:center;letter-spacing:4px}
.area{position:absolute;top:84px;width:160px;margin-left:-80px;text-align:center}
.area .ring{width:62px;height:62px;border-radius:50%;background:var(--navy);margin:0 auto;position:relative;display:flex;align-items:center;justify-content:center}
.area .num{position:absolute;bottom:-6px;left:50%;margin-left:-8px;width:16px;height:16px;border-radius:50%;background:var(--teal);color:#fff;font-size:6px;line-height:16px;font-weight:600}
.area .label{font-size:9px;font-weight:600;color:var(--navy);margin-top:18px;line-height:12px;text-transform:uppercase}
.area.on .ring{background:var(--white);border:4px solid var(--navy);box-shadow:0 0 0 3px #cfe9ef}
.area.on .ring span{font-size:18px;font-weight:600;color:var(--navy)}
.area.on .label{color:var(--teal)}

/* Network */
.net-head{top:1580px}
.net-head .title{margin-top:8px}
.net-head .lead{margin-top:10px}
.stat{position:absolute;top:1709px;width:221px;height:244px;text-align:center}
.stat .img{height:124px;position:relative}
.stat .img::after{content:"";position:absolute;left:50%;bottom:0;margin-left:-10px;border:10px solid transparent;border-bottom-color:var(--white);border-top:0}
.stat .n{font-size:25px;font-weight:600;color:var(--navy);margin-top:14px}
.stat .n.teal{color:var(--teal)}
.stat .k{font-size:8px;font-weight:700;letter-spacing:.6px;color:var(--navy);margin-top:4px}
.stat .d{font-size:10px;line-height:15px;color:var(--muted);margin:6px auto 0;width:190px}
.stat.raised{box-shadow:0 8px 18px rgba(0,0,0,.08)}
.img-a{background:linear-gradient(180deg,#5e6774,#2c333d)}
.img-b{background:linear-gradient(135deg,#cfd8e2,#6d8aa6 60%,#2f4256)}
.img-c{background:linear-gradient(180deg,#a6adb5,#5c636c)}
.img-d{background:linear-gradient(135deg,#4b535d,#1d2229)}

/* Themes band */
.themes{top:2024px;height:413px;background:linear-gradient(180deg,rgba(24,33,47,.82),rgba(24,33,47,.92)),linear-gradient(135deg,#55657a,#1f2a3a)}
.seal{position:absolute;left:50%;margin-left:-30px;width:60px;height:60px;border-radius:50%;background:var(--white);display:flex;align-items:center;justify-content:center}
.seal i{width:20px;height:20px;border-radius:50%;border:3px solid var(--teal);display:block}
.themes .copy{top:70px}
.themes .title{color:var(--white);margin-top:6px}
.themes .lead{color:#e3e7ec;width:460px;margin-top:10px}
.theme{position:absolute;top:226px;width:200px;margin-left:-100px;text-align:center}
.theme .ic{width:62px;height:62px;border-radius:50%;background:linear-gradient(135deg,#5fd3e4,#2ea6c2);margin:0 auto;display:flex;align-items:center;justify-content:center}
.theme .ic.white{background:var(--white)}
.theme p{color:var(--white);font-size:12px;font-weight:600;line-height:17px;margin-top:18px}
.theme.on p{color:var(--teal)}

/* Team */
.team{top:2437px;height:552px;background:linear-gradient(180deg,#fff 0%,#fff 60%,#eceff2 100%)}
.team .copy{top:65px}
.team .title{margin-top:6px}
.team .lead{margin-top:10px}
.filters{position:absolute;top:195px;left:0;width:1200px;display:flex;justify-content:center;gap:4px}
.filters span{font-size:8px;font-weight:600;letter-spacing:.6px;background:var(--navy);color:#fff;border-radius:12px;padding:7px 0;width:60px;text-align:center}
.filters span.wide{width:90px}
.filters span.on{background:var(--teal)}
.member{position:absolute;top:270px;width:200px;margin-left:-100px;text-align:center}
.member .pic{width:146px;height:146px;border-radius:50%;margin:0 auto;background:#fff;box-shadow:0 4px 14px rgba(0,0,0,.1);padding:6px}
.member .pic div{width:100%;height:100%;border-radius:50%;background:linear-gradient(180deg,#eef0f3,#b9c0c9);position:relative}
.member.on .pic div{background:radial-gradient(circle at 50% 40%,#6ed1e1,#2f9fb8)}
.member .tag{position:absolute;left:50%;bottom:30px;margin-left:-20px;background:#1b1f26;color:#fff;font-size:6px;padding:3px 5px}
.member h4{font-size:9px;font-weight:600;color:var(--navy);margin-top:22px;letter-spacing:.3px}
.member.on h4{color:var(--teal)}
.member p{font-size:9px;line-height:14px;color:var(--muted);margin-top:4px}

/* Engine */
.engine{top:3050px}
.engine .title{margin-top:6px}
.engine .lead{margin-top:10px;width:480px}
.ecard{position:absolute;top:3201px;width:301px;text-align:center}
.ecard .img{height:169px;position:relative}
.ecard .ico{position:absolute;left:50%;bottom:-16px;margin-left:-16px;width:32px;height:32px;border-radius:50%;background:#fff;display:flex;align-items:center;justify-content:center}
.ecard.raised{box-shadow:0 8px 20px rgba(0,0,0,.1);height:311px}
.ecard.raised .ico{bottom:auto;top:70px;background:var(--teal)}
.ecard h4{font-size:11px;font-weight:600;color:var(--navy);margin-top:34px;text-transform:uppercase;letter-spacing:.3px}
.ecard.raised h4{color:var(--teal);margin-top:24px}
.ecard p{font-size:10px;line-height:15px;color:var(--muted);width:250px;margin:6px auto 0}
.img-meet{background:linear-gradient(135deg,#eef1f4,#b5bfca 60%,#7c8895)}
.img-desk{background:linear-gradient(135deg,#7a7f86,#3c4148)}
.img-earth{background:radial-gradient(ellipse at 50% 90%,#7fb6e6,#28508a 30%,#0b1530 65%,#05070f)}

/* Contact band */
.contact{top:3577px;height:256px;background:linear-gradient(180deg,#1a2a4e,#142040 60%,#0f1830)}
.contact .copy{top:66px}
.contact .title{color:var(--white);margin-top:6px}
.contact .sub{color:#e3e7ec;font-size:10px;margin-top:8px}
.contact .btn{margin-top:18px}

/* Footer */
.footer{top:3833px;height:207px;background:var(--band);text-align:center}
.footer .brand{left:0;width:1200px;justify-content:center;top:48px}
.footer .copyright{position:absolute;top:96px;width:1200px;font-size:8px;color:#aeb6c1;letter-spacing:.5px}
.footer .links{position:absolute;top:113px;width:1200px;font-size:8px;font-weight:600;color:#fff;letter-spacing:.5px}
.footer .links span{margin:0 6px}
.footer .social{position:absolute;top:142px;left:0;width:1200px;display:flex;justify-content:center;gap:14px;align-items:center}
.footer .social i{width:12px;height:12px;border-radius:50%;background:#fff;display:block;opacity:.9}
.footer .social i.on{width:22px;height:22px;background:var(--teal);border:3px solid #fff}
.footer .tip{position:absolute;top:168px;left:544px;font-size:6px;background:#11161e;color:#fff;padding:2px 5px}
.footer .up{position:absolute;top:186px;left:595px}
</style>
</head>
<body>

<!-- Header + hero -->
<section class="section hero">
  <div class="hero-glow" role="img" aria-label="Glowing digital globe of data points in blue and purple"></div>
  <div class="brand" style="left:129px;top:35px"><span class="dot"></span>Lorvek Partners</div>
  <nav class="nav">
    <span class="active">HOME</span><span>ABOUT</span><span>FOCUS</span><span>NETWORK</span><span>THEMES</span><span>TEAM</span><span>GTM ENGINE</span>
    <span class="btn">✉ CONTACT US</span>
  </nav>
  <div class="center hero-copy">
    <div class="eyebrow">Networking &amp; Architecture</div>
    <h1 class="title">The VC With The Strongest GTM<br>Engine</h1>
    <p class="sub">We Invest in Enterprise IT Startups at the Product-Market-Fit Stage</p>
    <span class="btn">Explore More</span>
  </div>
  <svg style="position:absolute;left:594px;top:548px" width="12" height="8"><path d="M1 1l5 5 5-5" stroke="#8a93a8" fill="none" stroke-width="1.5"/></svg>
</section>

<!-- About -->
<div class="center about-head">
  <div class="eyebrow lined">About</div>
  <h2 class="title">Who We Are</h2>
  <p class="lead">We only invest in post-product, post-revenue Enterprise IT startups. Usually, this means you're at Seed Extension to Series A stage.</p>
</div>
<div class="tile photo-people" style="left:129px" role="img" aria-label="Two smiling business colleagues reviewing charts at a desk">
  <div class="cap">CUSTOMERS</div>
  <div class="tile-badge"><svg width="16" height="16" viewBox="0 0 16 16" fill="none" stroke="#555" stroke-width="1.3"><circle cx="8" cy="5" r="3"/><path d="M2 15c0-3.5 3-5 6-5s6 1.5 6 5"/></svg></div>
</div>
<div class="tile philosophy" style="left:450px">
  <div class="mark"></div>
  <h3>Our Investment<br>Philosophy</h3>
  <p>We only invest in startups that have broad &amp; immediate applicability across a global CIO base and are solving critical problems. To give our portfolio companies a truly unfair competitive advantage, we do not invest in competitive startups.</p>
  <div class="bulb"><svg width="14" height="14" viewBox="0 0 14 14" fill="none" stroke="#fff" stroke-width="1.3"><path d="M7 1a4 4 0 0 0-2.5 7.1V10h5V8.1A4 4 0 0 0 7 1zM5 12h4"/></svg></div>
</div>
<div class="tile photo-tower" style="left:769px" role="img" aria-label="Glass office tower seen from below against a cloudy sky">
  <div class="cap">INVESTMENTS</div>
  <div class="tile-badge"><svg width="16" height="16" viewBox="0 0 16 16" fill="none" stroke="#555" stroke-width="1.3"><path d="M1 14h14M2 11l4-4 3 2 5-5"/></svg></div>
</div>

<!-- Focus areas -->
<section class="section focus">
  <div class="eyebrow">Investment Focus Areas</div>
  <div class="area" style="left:199px"><div class="ring"><svg width="26" height="26" viewBox="0 0 26 26" fill="none" stroke="#fff" stroke-width="1.4"><rect x="7" y="7" width="12" height="12"/><path d="M10 3v4M16 3v4M10 19v4M16 19v4M3 10h4M3 16h4M19 10h4M19 16h4"/></svg><span class="num">01</span></div><div class="label">Security</div></div>
  <div class="area" style="left:359px"><div class="ring"><svg width="26" height="26" viewBox="0 0 26 26" fill="none" stroke="#fff" stroke-width="1.4"><circle cx="13" cy="13" r="9"/><path d="M13 4v18M6 9h14M6 17h14"/></svg><span class="num">02</span></div><div class="label">AI &amp; ML</div></div>
  <div class="area on" style="left:519px"><div class="ring"><span>03</span></div><div class="label">Networking &amp;<br>Architecture</div></div>
  <div class="area" style="left:679px"><div class="ring"><svg width="26" height="26" viewBox="0 0 26 26" fill="none" stroke="#fff" stroke-width="1.4"><path d="M7 17a5 5 0 0 1 1-9.9A6 6 0 0 1 19.5 9 4 4 0 0 1 19 17z"/><path d="M13 17v5M9 22h8"/></svg><span class="num">04</span></div><div class="label">Cloud &amp;<br>Infrastructure</div></div>
  <div class="area" style="left:839px"><div class="ring"><svg width="26" height="26" viewBox="0 0 26 26" fill="none" stroke="#fff" stroke-width="1.4"><circle cx="10" cy="15" r="5"/><circle cx="18" cy="8" r="3.5"/></svg><span class="num">05</span></div><div class="label">DevOps</div></div>
  <div class="area" style="left:999px"><div class="ring"><svg width="26" height="26" viewBox="0 0 26 26" fill="none" stroke="#fff" stroke-width="1.4"><rect x="4" y="6" width="18" height="14" rx="2"/><path d="M8 11h10M8 15h6"/></svg><span class="num">06</span></div><div class="label">SaaS</div></div>
</section>

<!-- Network -->
<div class="center net-head">
  <div class="eyebrow lined">Network</div>
  <h2 class="title">Strength In Numbers</h2>
  <p class="lead">We collect and analyze monthly purchase intent data from a global network of IT decision-makers.</p>
</div>
<div class="stat" style="left:129px"><div class="img img-a" role="img" aria-label="Silhouettes of executives standing by an office window"></div><div class="n">500+</div><div class="k">ADOPTING</div><p class="d">Early adopting, influential CIOs, CTOs, CISOs and IT decision-makers</p></div>
<div class="stat raised" style="left:369px"><div class="img img-b" role="img" aria-label="Hands using a tablet with financial charts"></div><div class="n teal">$100B+</div><div class="k">BUDGET</div><p class="d">Annual enterprise technology purchasing budget across our network</p></div>
<div class="stat" style="left:609px"><div class="img img-c" role="img" aria-label="Misty city skyline in grey tones"></div><div class="n">15</div><div class="k">NETWORK</div><p class="d">Countries represented in our current network</p></div>
<div class="stat" style="left:849px"><div class="img img-d" role="img" aria-label="Tunnel of binary digits in dark tones"></div><div class="n">550+</div><div class="k">DATA</div><p class="d">Purchase intent data points collected monthly</p></div>

<!-- Themes -->
<section class="section themes" role="img" aria-label="Night city skyline with connecting network lines, darkened">
  <div class="seal" style="top:-30px"><i></i></div>
  <div class="center copy">
    <div class="eyebrow">Themes</div>
    <h2 class="title">Unifying Investment</h2>
    <p class="lead">We are singularly focused on helping our portfolio companies gain a massive competitive advantage by providing them access to our exclusive network of hundreds of early-adopting CIOs, CTOs, CISOs, and Channel Partners around the world to rapidly accelerate customer traction.</p>
  </div>
  <div class="theme" style="left:318px"><div class="ic"><svg width="24" height="24" viewBox="0 0 24 24" fill="none" stroke="#fff" stroke-width="1.4"><circle cx="12" cy="12" r="9"/><path d="M3 12h18M12 3c3 3 3 15 0 18M12 3c-3 3-3 15 0 18"/></svg></div><p>Next-Gen Enterprise<br>IT Solutions</p></div>
  <div class="theme on" style="left:600px"><div class="ic white"><svg width="24" height="24" viewBox="0 0 24 24" fill="none" stroke="#3bbfd6" stroke-width="2"><circle cx="12" cy="12" r="8"/></svg></div><p>Attacking Large Markets<br>With Universal Application</p></div>
  <div class="theme" style="left:880px"><div class="ic"><svg width="24" height="24" viewBox="0 0 24 24" fill="none" stroke="#fff" stroke-width="1.4"><path d="M4 7h16M4 12h16M4 17h16"/></svg></div><p>Products And Platforms That<br>Take A Holistic Approach</p></div>
</section>

<!-- Team -->
<section class="section team">
  <div class="center copy">
    <div class="eyebrow lined">Team</div>
    <h2 class="title">Team, Investors &amp; Advisors</h2>
    <p class="lead">We have built a world-class roster of executive advisors and mentors with exceptional go-to-market pedigrees to help our portfolio companies in their go-to-market journeys.</p>
  </div>
  <div class="filters"><span>ALL</span><span class="on">TEAM</span><span class="wide">INVESTORS</span><span class="wide">ADVISORS</span></div>
  <div class="member" style="left:245px"><div class="pic"><div role="img" aria-label="Portrait of the founder and managing director"></div></div><h4>RAFIQ N. DOVAN</h4><p>Founder &amp; Managing Director</p></div>
  <div class="member on" style="left:480px"><div class="pic"><div role="img" aria-label="Portrait of a team member with teal hover overlay"><span class="tag">View Bio</span></div></div><h4>COLIN AVERETT</h4><p>Founder &amp; Ex CEO,<br>Corvanta</p></div>
  <div class="member" style="left:715px"><div class="pic"><div role="img" aria-label="Portrait of a co-founder"></div></div><h4>DEVAN MEHRA</h4><p>Co-founder,<br>Stratyx (IPO), Querylight</p></div>
  <div class="member" style="left:951px"><div class="pic"><div role="img" aria-label="Portrait of a co-founder"></div></div><h4>ILAN BOTREV</h4><p>Co-founder,<br>Lakefin ($2B+ valuation)</p></div>
</section>

<!-- Engine -->
<div class="center engine">
  <div class="eyebrow lined">Engine</div>
  <h2 class="title">A Global GTM Engine</h2>
  <p class="lead">We don't just make "customer intros", we partner with you each step of the way to help you navigate the complex landscape of enterprise sales, from key strategic accounts to strategic channel partners</p>
</div>
<div class="ecard" style="left:129px"><div class="img img-meet" role="img" aria-label="Team meeting in a bright office with charts on a screen"><div class="ico"><svg width="14" height="14" viewBox="0 0 14 14" fill="none" stroke="#555" stroke-width="1.2"><rect x="1" y="2" width="12" height="8"/><path d="M5 13h4M7 10v3"/></svg></div></div><h4>GTM Coaches</h4><p>We will partner with you to navigate the complex enterprise sales process by leveraging our executive network to provide product feedback, sales strategy, and market insights</p></div>
<div class="ecard raised" style="left:450px"><div class="img img-desk" role="img" aria-label="Desk with documents and a laptop in grey tones"><div class="ico"><svg width="14" height="14" viewBox="0 0 14 14" fill="none" stroke="#fff" stroke-width="1.3"><circle cx="7" cy="3" r="1.5"/><path d="M7 4.5V13M3 8a4 4 0 0 0 8 0M5 6h4"/></svg></div></div><h4>Strategic Partners</h4><p>Strategic partnerships can propel a startup to the next level. Leverage our extensive network of IT Executives, Channel Partners, and OEMs to accelerate your path to becoming a category leader</p></div>
<div class="ecard" style="left:769px"><div class="img img-earth" role="img" aria-label="Earth from space at night with glowing city lights"><div class="ico"><svg width="14" height="14" viewBox="0 0 14 14" fill="none" stroke="#555" stroke-width="1.2"><circle cx="7" cy="7" r="5.5"/><path d="M1.5 7h11M7 1.5c2 2 2 9 0 11M7 1.5c-2 2-2 9 0 11"/></svg></div></div><h4>Global Ambassadors</h4><p>Expanding globally is no simple exercise. Our network of Global IT Execs will provide on-the-ground intelligence, referrals, and influence as you conquer new geographies</p></div>

<!-- Contact -->
<section class="section contact" role="img" aria-label="Night skyline with glowing network connections in deep blue">
  <div class="seal" style="top:-30px"><i></i></div>
  <div class="center copy">
    <div class="eyebrow lined">Support</div>
    <h2 class="title">Contact Us For Anything</h2>
    <p class="sub">Someone on our team will email you within a few days in regards to your message.</p>
    <span class="btn">✉ Contact Us</span>
  </div>
</section>

<!-- Footer -->
<footer class="section footer">
  <div class="brand"><span class="dot"></span>Lorvek Partners</div>
  <div class="copyright">COPYRIGHT © 2022 LORVEK PARTNERS</div>
  <div class="links"><span>PRIVACY POLICY</span>|<span>TERMS &amp; CONDITIONS</span></div>
  <div class="social"><i class="on"></i><i></i><i></i><i></i></div>
  <div class="tip">Profile</div>
  <svg class="up" width="10" height="6"><path d="M1 5l4-4 4 4" stroke="#8a93a8" fill="none" stroke-width="1.3"/></svg>
</footer>

</body>
</html>
```